Business card design for strategy and management consulting company. Would like to have a clean and professional business card, based on the attached logo. The company is a strategy and management consulting company focusing on sustainable business modlels based on economic, social and environmental market opportunities. Preferably the logo should be included on both sides of the design.

Industry/Entity Type

Business

Contact Information for Business Card

Håvard Lilleby, CEO/Management consultant
havard.lilleby@quarvenpartners.example
Mob: +47 948 26 317
Office: Vikfjell gate 14, pb 312 sentrum, N-0172 Oslo Norway

Requirements
Must have
• Include attached logo
Nice to have
• Would like to have the logo on both sides
Should not have
• Many colours.

```html
<!DOCTYPE html>
<html lang="en">
<head>
<meta charset="utf-8">
<title>Quarven business card</title>
<link rel="stylesheet" href="https://fonts.googleapis.com/css2?family=Lato:wght@400;700;900&display=swap">
<style>
  :root {
    --stage: #2c2c2c;
    --card-dark: #1e1e1e;
    --card-mid: #2f2f2f;
    --card-light: #444444;
    --ink-white: #ffffff;
    --ink-grey: #d6d6d6;
    --accent: #f5d90a;
  }
  * { margin: 0; padding: 0; box-sizing: border-box; }
  html, body { width: 1200px; height: 900px; overflow: hidden; }
  body {
    background: radial-gradient(ellipse at 40% 30%, #3a3a3a 0%, var(--stage) 70%);
    font-family: "Lato", sans-serif;
    position: relative;
  }
  .card {
    position: absolute;
    top: 290px;
    width: 520px;
    height: 320px;
    overflow: hidden;
  }
  .card--front {
    left: 50px;
    background: linear-gradient(160deg, var(--card-mid) 0%, var(--card-dark) 100%);
  }
  .card--back {
    left: 630px;
    background: linear-gradient(160deg, var(--card-dark) 0%, var(--card-light) 45%, var(--card-dark) 100%);
  }
  .wordmark {
    display: flex;
    align-items: center;
    gap: 10px;
    color: var(--ink-white);
    font-weight: 900;
    letter-spacing: -1px;
    line-height: 1;
  }
  .wordmark__dot {
    width: 10px; height: 10px;
    border-radius: 50%;
    background: var(--accent);
  }
  .card--front .wordmark {
    position: absolute;
    left: 36px; top: 30px;
    font-size: 54px;
  }
  .card--back .wordmark {
    position: absolute;
    left: 50%; top: 50%;
    transform: translate(-50%, -50%);
    font-size: 86px;
  }
  .card--back .wordmark__dot { width: 14px; height: 14px; }
  .holder {
    position: absolute;
    left: 36px; top: 100px;
  }
  .holder__name {
    color: var(--accent);
    font-weight: 700;
    font-size: 21px;
  }
  .holder__title {
    color: var(--ink-grey);
    font-size: 15px;
    margin-top: 3px;
  }
  .contact {
    position: absolute;
    left: 36px; top: 172px;
    list-style: none;
    color: var(--ink-grey);
    font-size: 15px;
    line-height: 1.5;
  }
  .contact__row { display: flex; align-items: center; gap: 8px; }
  .contact__row--plain { padding-left: 0; }
  .contact__icon { width: 13px; height: 13px; flex: none; }
  .accent-band {
    position: absolute;
    left: 0; right: 0; bottom: 0;
    height: 7px;
    background: var(--accent);
  }
</style>
</head>
<body>
  <section class="card card--front" aria-label="Card front">
    <div class="wordmark">Quarven<span class="wordmark__dot"></span></div>
    <div class="holder">
      <p class="holder__name">Håvard Lilleby</p>
      <p class="holder__title">CEO/Management consultant</p>
    </div>
    <ul class="contact">
      <li class="contact__row">
        <svg class="contact__icon" viewBox="0 0 13 13" aria-hidden="true">
          <rect x="3" y="0.5" width="7" height="12" rx="1.2" fill="none" stroke="#f5d90a" stroke-width="1.3"/>
          <rect x="5.5" y="10" width="2" height="1" fill="#f5d90a"/>
        </svg>
        +47 948 26 317
      </li>
      <li class="contact__row">
        <svg class="contact__icon" viewBox="0 0 13 13" aria-hidden="true">
          <rect x="0.5" y="2.5" width="12" height="8" fill="#f5d90a"/>
          <path d="M0.5 2.5 L6.5 7 L12.5 2.5" fill="none" stroke="#1e1e1e" stroke-width="1.2"/>
        </svg>
        havard.lilleby@quarvenpartners.example
      </li>
      <li class="contact__row contact__row--plain">Vikfjell gate 14</li>
      <li class="contact__row contact__row--plain">PB 312 Sentrum, 0172 Oslo Norway</li>
    </ul>
    <div class="accent-band"></div>
  </section>

  <section class="card card--back" aria-label="Card back">
    <div class="wordmark">Quarven<span class="wordmark__dot"></span></div>
  </section>
</body>
</html>
```